Consulting Company Business Card

I am looking for a minimalist, classy, professional design on my business card. I would like it to be double-sided. I want to use the font and color scheme of my logo which are attached. Please be creative in the designs that you send me. I want to play off the design of my logo with the inner C that is Green and Blue broken up with the white.
Target Market(s)
Small Businesses
Industry/Entity Type
Consulting
Contact Information for Business Card
Dale M. Whitcombe, CPA CGMA, 555-014-2873, dwhitcombe@vorantaadvisory.example, www.vorantaadvisory.example

```html
<!DOCTYPE html>
<html lang="en">
<head>
<meta charset="utf-8">
<title>Voranta Advisory Business Card</title>
<link href="https://fonts.googleapis.com/css2?family=Montserrat:wght@400;500;600;700&display=swap" rel="stylesheet">
<style>
  :root {
    --page: #f4f4f4;
    --card: #fbfbfb;
    --card-shade: #e9eaeb;
    --navy: #1f3a68;
    --teal: #1b8a86;
    --ink: #4a4f57;
    --muted: #6b7079;
  }
  * { margin: 0; padding: 0; box-sizing: border-box; }
  html, body { width: 735px; height: 1200px; overflow: hidden; background: var(--page); }
  body { font-family: "Montserrat", sans-serif; color: var(--ink); position: relative; }

  .card {
    position: absolute;
    left: 57px;
    width: 620px;
    height: 354px;
    background: var(--card);
    box-shadow: 0 3px 12px rgba(0,0,0,0.12);
    overflow: hidden;
  }
  .card--front { top: 210px; }
  .card--back { top: 640px; }

  .card__texture {
    position: absolute;
    right: 0; top: 0;
    width: 60%; height: 100%;
    background: linear-gradient(115deg, rgba(255,255,255,0) 30%, var(--card-shade) 100%);
  }

  .card__stripe { position: absolute; left: 0; bottom: 0; width: 620px; height: 18px; }

  .brand { position: absolute; display: flex; align-items: center; gap: 10px; }
  .brand__dot { width: 14px; height: 14px; border-radius: 50%; background: var(--teal); }
  .brand__name {
    font-weight: 700;
    color: var(--navy);
    letter-spacing: 1px;
    text-transform: uppercase;
  }

  .card--front .brand { top: 132px; left: 0; width: 100%; justify-content: center; }
  .card--front .brand__name { font-size: 30px; }
  .front__web {
    position: absolute; top: 218px; width: 100%; text-align: center;
    font-size: 11px; color: var(--muted); letter-spacing: 0.4px;
  }

  .card--back .brand { top: 60px; right: 48px; }
  .card--back .brand__name { font-size: 20px; }

  .holder { position: absolute; left: 46px; top: 168px; }
  .holder__name {
    font-size: 23px; font-weight: 600; color: var(--teal);
    text-transform: uppercase; letter-spacing: 0.8px;
  }
  .holder__title { font-size: 11px; font-weight: 500; color: var(--muted); margin-top: 4px; letter-spacing: 0.5px; }

  .contact { position: absolute; left: 46px; top: 236px; list-style: none; }
  .contact__item { display: flex; align-items: center; gap: 9px; font-size: 11px; color: var(--muted); margin-bottom: 8px; }
  .contact__icon { width: 10px; height: 10px; flex: none; }
</style>
</head>
<body>

<section class="card card--front" aria-label="Card front">
  <div class="card__texture" role="img" aria-label="Subtle diagonal line texture"></div>
  <div class="brand">
    <span class="brand__dot"></span>
    <span class="brand__name">Voranta Advisory</span>
  </div>
  <p class="front__web">www.vorantaadvisory.example</p>
  <svg class="card__stripe" viewBox="0 0 620 18" aria-hidden="true">
    <rect x="0" y="13" width="330" height="3" fill="var(--teal)"/>
    <polygon points="338,6 620,6 620,18 326,18" fill="var(--navy)"/>
  </svg>
</section>

<section class="card card--back" aria-label="Card back">
  <div class="card__texture" role="img" aria-label="Subtle diagonal line texture"></div>
  <div class="brand">
    <span class="brand__dot"></span>
    <span class="brand__name">Voranta Advisory</span>
  </div>
  <div class="holder">
    <h1 class="holder__name">Dale M. Whitcombe</h1>
    <p class="holder__title">CPA CGMA</p>
  </div>
  <ul class="contact">
    <li class="contact__item">
      <svg class="contact__icon" viewBox="0 0 10 10"><path d="M2 0.5 L4 2.5 L3 3.8 Q4.3 6 6.2 7 L7.5 6 L9.5 8 L8 9.5 Q3.5 9 0.5 2 Z" fill="var(--teal)"/></svg>
      555-014-2873
    </li>
    <li class="contact__item">
      <svg class="contact__icon" viewBox="0 0 10 10"><rect x="0.5" y="2" width="9" height="6.5" fill="none" stroke="var(--teal)" stroke-width="1.2"/><path d="M0.5 2 L5 5.5 L9.5 2" fill="none" stroke="var(--teal)" stroke-width="1.2"/></svg>
      dwhitcombe@vorantaadvisory.example
    </li>
    <li class="contact__item">
      <svg class="contact__icon" viewBox="0 0 10 10"><circle cx="5" cy="5" r="4.3" fill="none" stroke="var(--teal)" stroke-width="1.1"/><path d="M0.7 5 H9.3 M5 0.7 Q2.5 5 5 9.3 M5 0.7 Q7.5 5 5 9.3" fill="none" stroke="var(--teal)" stroke-width="0.9"/></svg>
      www.vorantaadvisory.example
    </li>
  </ul>
  <svg class="card__stripe" viewBox="0 0 620 18" aria-hidden="true">
    <rect x="0" y="13" width="330" height="3" fill="var(--teal)"/>
    <polygon points="338,6 620,6 620,18 326,18" fill="var(--navy)"/>
  </svg>
</section>

</body>
</html>
```